Locksmith SmartPhone Web Design Project

I am a locksmith and focus on customers that use their smart phones to find me. I have a static web page that I created myself but it is horrible. See for yourself at www.tarvelmacks.com.au

I want a cross-platform static site that simply shows the information and with the ability to change minor items like pricing. I want it to be compelling in its look and feel (not overwhelming) but simple. It must have a; click to call button; the ability to install a hit counter from zorbiqly.com; payment information just like the current graphic of card/cash/quenzo (lumo/brevindale only).

This will be hosted on my own server.
Updates

Hello Designers,

I have updated the brief in the must have and nice to have fields.

Thank you all,

Toby.

Hello to all Designers,

There is about 9 days left before the deadline. The overall level of competition is extremely high and I would like to thank all the designers who have submitted so far, 27 submissions in total so far. Excellent work.

If you have submitted already and wish to provide new designs, I am keen to see them. 

Hi guys, time is almost up. Please submit any new designs that you may have. The quality has been excellent so far.

Toby.

Target Market(s)

People who are locked out of their house/shop/office etc.

Industry/Entity Type

Locksmith

Requirements
Must have
• click to call button
hit counter from zorbiqly
payment graphic card/cash/quenzo (lumo/brevindale only)
cross platform compatibility smartphone/phablet
Single column page preferable, can have two columns.
Nice to have
• When the page loads regardless of the mobile device, all info should be presented. In other words no vertical or horizontal scroll bars.
Should not have
• hidden code, advertising, credits etc

```html
<!DOCTYPE html>
<html lang="en">
<head>
<meta charset="utf-8">
<title>Tarvelmacks Locksmiths</title>
<link href="https://fonts.googleapis.com/css2?family=PT+Sans+Narrow:wght@700&family=PT+Sans:wght@400;700&family=Open+Sans:wght@400&display=swap" rel="stylesheet">
<style>
  :root {
    --page-bg: #e6e6e6;
    --screen-bg: #f5f5f5;
    --header-top: #0aa4f2;
    --header-bottom: #0878d6;
    --headline: #454545;
    --body-text: #5a5a5a;
    --accent-blue: #1565a8;
    --rule: #d2d2d2;
    --button-top: #fbfbfb;
    --button-bottom: #dcdcdc;
    --button-ring: #bdbdbd;
    --badge-text: #1d3f8a;
    --white: #ffffff;
  }
  * { margin: 0; padding: 0; box-sizing: border-box; }
  html, body {
    width: 1200px; height: 900px; overflow: hidden;
    background: var(--page-bg);
  }
  .screen {
    position: absolute; left: 284px; top: 0;
    width: 640px; height: 900px;
    background: var(--screen-bg);
    overflow: hidden;
  }
  .site-header {
    height: 86px;
    background: linear-gradient(var(--header-top), var(--header-bottom));
    display: flex; align-items: center; justify-content: center;
  }
  .site-title {
    font-family: "PT Sans Narrow", sans-serif; font-weight: 700;
    color: var(--white); font-size: 38px; letter-spacing: 0.5px;
    text-transform: uppercase;
  }
  .headline {
    position: absolute; top: 128px; left: 0; width: 640px;
    text-align: center;
    font-family: "PT Sans Narrow", sans-serif; font-weight: 700;
    font-size: 50px; line-height: 68px; color: var(--headline);
    text-transform: uppercase;
  }
  .locksmith-photo {
    position: absolute; left: 20px; top: 292px;
    width: 197px; height: 180px;
    border: 6px solid var(--white); border-radius: 12px;
    box-shadow: 0 2px 5px rgba(0,0,0,0.35);
    background: linear-gradient(160deg, #a8262c 0%, #8a2a3a 45%, #1f7fcf 100%);
  }
  .service-name, .clock-line {
    position: absolute; left: 243px;
    font-family: "Open Sans", sans-serif; font-size: 27px; color: var(--body-text);
  }
  .service-name { top: 328px; }
  .clock-line { top: 388px; display: flex; align-items: center; gap: 20px; }
  .clock-line svg { width: 44px; height: 44px; }
  .rule {
    position: absolute; left: 30px; width: 568px; height: 2px; background: var(--rule);
  }
  .rule-top { top: 520px; }
  .rule-bottom { top: 893px; left: 38px; }
  .availability {
    position: absolute; top: 560px; left: 0; width: 640px; text-align: center;
    font-family: "PT Sans", sans-serif; font-weight: 700; font-size: 35px;
    color: var(--accent-blue); word-spacing: 2px;
  }
  .call-button {
    position: absolute; left: 62px; top: 655px; width: 518px; height: 71px;
    border-radius: 36px; border: 5px solid var(--button-ring);
    background: linear-gradient(var(--button-top), var(--button-bottom));
    display: flex; align-items: center; justify-content: center; gap: 20px;
    font-family: "PT Sans", sans-serif; font-weight: 700; font-size: 31px;
    color: var(--accent-blue); text-decoration: none;
    box-shadow: 0 2px 4px rgba(0,0,0,0.15);
  }
  .call-button svg { width: 30px; height: 30px; }
  .payment-list {
    position: absolute; top: 783px; left: 92px; width: 456px;
    display: flex; justify-content: space-between; list-style: none;
  }
  .payment-badge {
    width: 66px; height: 42px; border-radius: 4px;
    background: linear-gradient(#ffffff, #d9d9d9);
    border: 1px solid #b5b5b5;
    box-shadow: 0 3px 3px rgba(0,0,0,0.35);
    display: flex; align-items: center; justify-content: center; text-align: center;
    font-family: "PT Sans", sans-serif; font-weight: 700; font-size: 13px;
    line-height: 13px; color: var(--badge-text);
  }
  .payment-badge.is-small { font-size: 10px; }
  .payment-badge.is-bank { font-size: 19px; }
</style>
</head>
<body>
  <main class="screen">
    <header class="site-header">
      <h1 class="site-title">Tarvelmacks Locksmiths</h1>
    </header>

    <h2 class="headline">Locked out?<br>$150 gets you in. Easy!</h2>

    <div class="locksmith-photo" role="img" aria-label="Portrait photo of the locksmith"></div>
    <p class="service-name">Locksmith Lockout Service</p>
    <p class="clock-line">
      <svg viewBox="0 0 44 44" aria-hidden="true">
        <circle cx="22" cy="24" r="14" fill="none" stroke="#222" stroke-width="3.5"/>
        <path d="M5 12a8 8 0 0 1 10-7z M39 12a8 8 0 0 0-10-7z" fill="#222"/>
        <path d="M22 15v10h7" fill="none" stroke="#222" stroke-width="3" stroke-linecap="round"/>
        <path d="M12 36l-4 5 M32 36l4 5" stroke="#222" stroke-width="3.5" stroke-linecap="round"/>
      </svg>
      It is now 1:03:49 AM
    </p>

    <div class="rule rule-top"></div>

    <p class="availability">Locksmith Available?&nbsp; YES</p>

    <a class="call-button" href="tel:0428317905">
      <svg viewBox="0 0 24 24" aria-hidden="true">
        <path fill="#444" d="M6.6 10.8a15.1 15.1 0 0 0 6.6 6.6l2.2-2.2c.3-.3.7-.4 1-.2 1.1.4 2.3.6 3.6.6.6 0 1 .4 1 1V20c0 .6-.4 1-1 1A17 17 0 0 1 3 4c0-.6.4-1 1-1h3.5c.6 0 1 .4 1 1 0 1.3.2 2.5.6 3.6.1.3 0 .7-.2 1z"/>
      </svg>
      Click to Call : 0428317905
    </a>

    <ul class="payment-list">
      <li class="payment-badge">Quenzo</li>
      <li class="payment-badge">Money<br>Order</li>
      <li class="payment-badge is-small">Brevindale</li>
      <li class="payment-badge">Corvane</li>
      <li class="payment-badge is-bank">Bank</li>
    </ul>

    <div class="rule rule-bottom"></div>
  </main>
</body>
</html>
```